Company Introduction/Advertisement Flyer

We would like to redesign our current company line card. We send this printed flyer to prospective customers to introduce our company, the brands we represent and our competitive advantages. Our current design is very plain and simple, we'd like to have a little more design to the new version. Our website is www.valvequarryhub.com. We're a specialty supplier for plumbing material, specifically water and life safety products. Our customers are mostly male, blue-collar contractors, ages 40-60. I have included a pdf of our current flyer, and our high resolution transparent logo.

Requirements
Must have
• Phone number: (800) 314-2760
Website: www.valvequarryhub.com

```html
<!DOCTYPE html>
<html lang="en">
<head>
<meta charset="utf-8">
<title>Keystone Flowline Supply Company – Line Card</title>
<link href="https://fonts.googleapis.com/css2?family=Fira+Sans+Condensed:wght@500;700&family=Fira+Sans:wght@700&family=Oswald:wght@500&family=Open+Sans:wght@400&family=Roboto:wght@900&display=swap" rel="stylesheet">
<style>
  :root{
    --brand-blue:#1f5aa8;
    --brand-red:#e63946;
    --teal-deep:#0f6c79;
    --teal-mid:#2b8793;
    --teal-soft:#9fbcc6;
    --mist:#f3f6f7;
    --tile:#dbe8eb;
    --white:#ffffff;
    --ink:#2a3a44;
  }
  *{margin:0;padding:0;box-sizing:border-box}
  html,body{width:927px;height:1200px;overflow:hidden;background:var(--white)}
  .flyer{position:relative;width:927px;height:1200px;overflow:hidden;background:var(--white)}

  .masthead{position:absolute;left:95px;top:44px;display:flex;align-items:center;gap:18px}
  .masthead-mark{width:70px;height:70px;background:var(--brand-blue)}
  .masthead-name{font-family:"Open Sans",sans-serif;font-weight:400;color:var(--brand-blue);line-height:1}
  .masthead-name .line-main{display:block;font-size:48px;letter-spacing:-0.5px}
  .masthead-name .line-sub{display:block;font-size:24px;margin-top:6px}

  .backdrop{position:absolute;left:0;top:158px;width:927px;height:1042px;
    background:linear-gradient(155deg,var(--teal-deep) 0%,var(--teal-mid) 32%,var(--teal-soft) 62%,var(--mist) 88%)}
  .backdrop-facet{position:absolute;background:rgba(255,255,255,0.10);border-radius:40px;transform:rotate(45deg)}

  .source-band{position:absolute;left:0;top:158px;width:592px;height:43px;background:var(--brand-red);
    clip-path:polygon(0 0,100% 0,calc(100% - 20px) 100%,0 100%)}
  .source-band h2{font-family:"Fira Sans",sans-serif;font-weight:700;font-size:25px;color:var(--white);
    line-height:43px;padding-left:51px}

  .offer-list{position:absolute;left:52px;top:205px;list-style:none;font-family:"Fira Sans Condensed",sans-serif;
    font-weight:700;font-size:25px;color:var(--white);line-height:34px}
  .offer-list li::before{content:"•";margin-right:10px}

  .perks{position:absolute;left:54px;top:289px;list-style:none;font-family:"Fira Sans Condensed",sans-serif;
    font-weight:500;font-size:22.5px;color:var(--white);line-height:33px}
  .perks li::before{content:"•";font-size:14px;margin-right:6px;vertical-align:3px}
  .perks .cont{padding-left:11px}
  .perks .cont::before{content:none}

  .support{position:absolute;left:48px;top:518px;color:var(--white)}
  .support p{font-family:"Roboto",sans-serif;font-weight:900;font-size:18px;line-height:18px;letter-spacing:.3px}
  .support p::before{content:"•";margin-right:8px}
  .support p span{display:block;padding-left:18px}
  .support .phone{font-family:"Oswald",sans-serif;font-weight:500;font-size:35px;line-height:44px;padding-left:17px;margin-top:4px;display:block}

  .website{position:absolute;left:49px;top:626px;font-family:"Fira Sans",sans-serif;font-weight:700;
    font-size:22px;color:var(--white);letter-spacing:.4px}

  .product-tile{position:absolute;border-radius:24px;transform:rotate(45deg);overflow:hidden}
  .tile-gate{left:570px;top:155px;width:141px;height:141px;background:radial-gradient(circle,#c9463d 0%,#d98c86 30%,var(--tile) 60%)}
  .tile-parts{left:708px;top:245px;width:170px;height:170px;background:radial-gradient(circle,#8d8e8a 0%,#a9acaa 55%,#c6cbcc 100%)}
  .tile-clamp{left:482px;top:301px;width:134px;height:134px;background:radial-gradient(circle,#8d8f92 0%,#c4ccd0 35%,var(--tile) 65%)}
  .tile-testkit{left:616px;top:397px;width:141px;height:141px;background:radial-gradient(circle,#3a3f42 0%,#8a9599 35%,var(--tile) 65%)}
  .tile-case{left:753px;top:501px;width:141px;height:141px;background:radial-gradient(circle,#2d2f31 0%,#7d8589 30%,var(--tile) 60%)}
  .tile-lid{left:517px;top:531px;width:141px;height:141px;background:radial-gradient(circle,#b7b9b8 0%,#5e5a57 45%,#3c3a39 80%)}
  .tile-butterfly{left:655px;top:635px;width:141px;height:141px;background:radial-gradient(circle,#2b2b2b 0%,#7e8487 35%,var(--tile) 65%)}
  .tile-seat{left:431px;top:695px;width:170px;height:170px;background:radial-gradient(circle,#8a6d49 0%,#a99277 40%,#b9b6b2 80%)}
  .tile-gaugekit{left:595px;top:818px;width:177px;height:177px;background:radial-gradient(circle,#6f726b 0%,#b3b9b7 35%,var(--tile) 65%)}

  .warehouse{position:absolute;left:0;top:0;width:927px;height:1200px;pointer-events:none}

  .brand-grid{position:absolute;left:515px;top:1072px;width:388px;display:grid;gap:3px;
    background:#e2e9ec;padding:3px}
  .brand-row{display:grid;gap:3px}
  .row-four{grid-template-columns:repeat(4,1fr)}
  .row-five{grid-template-columns:repeat(5,1fr)}
  .brand-cell{background:var(--white);height:34px;display:flex;align-items:center;justify-content:center;
    font-family:"Fira Sans Condensed",sans-serif;font-weight:700;font-size:13px;color:var(--ink);white-space:nowrap}
</style>
</head>
<body>
<main class="flyer">

  <header class="masthead">
    <div class="masthead-mark" aria-hidden="true"></div>
    <h1 class="masthead-name">
      <span class="line-main">Keystone Flowline</span>
      <span class="line-sub">Supply Company</span>
    </h1>
  </header>

  <div class="backdrop">
    <div class="backdrop-facet" style="left:330px;top:380px;width:280px;height:280px"></div>
    <div class="backdrop-facet" style="left:800px;top:740px;width:200px;height:200px"></div>
  </div>

  <div class="source-band"><h2>Your Complete Source For</h2></div>

  <ul class="offer-list">
    <li>Backflow Preventer Repair Parts Accessories</li>
    <li>Enclosures Test Gauge Calibration</li>
  </ul>

  <ul class="perks">
    <li>Save gas and time by receiving</li>
    <li class="cont">parts at your doorstep</li>
    <li>1-2 day delivery anywhere in the country</li>
    <li>Same day shipping • No minimum orders</li>
    <li>Online tracking of your order</li>
    <li>Friendly, knowledgable staff</li>
  </ul>

  <div class="support">
    <p>Technicians available <span>to answer questions</span></p>
    <span class="phone">(800) 314-2760</span>
  </div>

  <p class="website">Website: www.valvequarryhub.com</p>

  <div class="product-tile tile-gate" role="img" aria-label="Red flanged gate valve with handwheel"></div>
  <div class="product-tile tile-parts" role="img" aria-label="Brass backflow valve parts and tools on concrete"></div>
  <div class="product-tile tile-clamp" role="img" aria-label="T-handle spring compression tool"></div>
  <div class="product-tile tile-testkit" role="img" aria-label="Backflow test kit in open case with hoses and gauge"></div>
  <div class="product-tile tile-case" role="img" aria-label="Black case with valve seat wrench plates"></div>
  <div class="product-tile tile-lid" role="img" aria-label="Technician removing a valve cover clamp"></div>
  <div class="product-tile tile-butterfly" role="img" aria-label="Black butterfly valve with red handwheel"></div>
  <div class="product-tile tile-seat" role="img" aria-label="Hand installing a check seat in a bronze valve body"></div>
  <div class="product-tile tile-gaugekit" role="img" aria-label="Grey test kit case with gauge and coloured hoses"></div>

  <svg class="warehouse" viewBox="0 0 927 1200" role="img" aria-label="Warehouse shelving stocked with boxed parts and an orange rolling ladder">
    <defs>
      <linearGradient id="warehouseTone" x1="0" y1="0" x2="1" y2="1">
        <stop offset="0" stop-color="#cfa97e"/>
        <stop offset="0.5" stop-color="#a58a6c"/>
        <stop offset="1" stop-color="#7a6f66"/>
      </linearGradient>
    </defs>
    <path d="M0 900 L205 775 Q222 764 238 776 L515 990 Q530 1004 520 1022 L425 1200 L0 1200 Z" fill="url(#warehouseTone)"/>
  </svg>

  <section class="brand-grid" aria-label="Brands we represent">
    <div class="brand-row row-four">
      <div class="brand-cell">Ferrox</div>
      <div class="brand-cell">Corvale</div>
      <div class="brand-cell">Arden</div>
      <div class="brand-cell">Plainsmeter</div>
    </div>
    <div class="brand-row row-four">
      <div class="brand-cell">Wexley</div>
      <div class="brand-cell">Dunmore Flow</div>
      <div class="brand-cell">Whitcombe</div>
      <div class="brand-cell">HeatVault</div>
    </div>
    <div class="brand-row row-five">
      <div class="brand-cell">Calvane</div>
      <div class="brand-cell">Orin</div>
      <div class="brand-cell">Halsted</div>
      <div class="brand-cell">Raincrest</div>
      <div class="brand-cell">SureShield</div>
    </div>
  </section>

</main>
</body>
</html>
```